Design Business Card with our Logo

We have changed our firm name from Halbrook, Tessing & Varn, PLLC to Halbrook, Tessing & Orlow, LLP and now need to re-design our business cards. I have attached an image of our old card so that you can see the style that we like -- clean, modern, colorful and professional. We were not thrilled with the fonts that we used on the old card, so feel free to use more modern fonts. I also attached a copy of the new logo shape, which is similar to the old one; and some other card ideas that we found in the gigmarto.com showcase that looked nice to us. Please feel free to try different colors as we are not tied down to orange or blue. Looking for fresh new ideas.

```html
<!DOCTYPE html>
<html lang="en">
<head>
<meta charset="utf-8">
<title>Halbrook, Tessing &amp; Orlow, LLP — Business Card</title>
<link rel="stylesheet" href="https://fonts.googleapis.com/css2?family=Roboto+Condensed:wght@400;700&family=Open+Sans:wght@400;600&display=swap">
<style>
  :root {
    --orange: #f05423;
    --ink: #6d6e71;
    --ink-dark: #4a4b4d;
    --paper: #ffffff;
    --paper-shade: #eeeeee;
    --backdrop: #a9a9a9;
  }
  * { box-sizing: border-box; margin: 0; padding: 0; }
  html, body { width: 1200px; height: 900px; overflow: hidden; }
  body {
    background: var(--backdrop);
    font-family: "Open Sans", sans-serif;
    color: var(--ink);
    position: relative;
  }
  .card {
    position: absolute;
    left: 290px;
    width: 620px;
    height: 354px;
    background: var(--paper);
    overflow: hidden;
    box-shadow: 0 6px 18px rgba(0,0,0,.18);
  }
  .card--front { top: 56px; }
  .card--back { top: 490px; }
  .card__texture {
    position: absolute; inset: 0;
    background:
      radial-gradient(circle at 25% 30%, var(--paper-shade) 0, transparent 45%),
      radial-gradient(circle at 75% 70%, var(--paper-shade) 0, transparent 50%),
      var(--paper);
  }
  .band { position: absolute; background: var(--orange); }

  /* Front */
  .card--front .band--top { left: 0; top: 0; width: 170px; height: 22px; }
  .card--front .band--bottom { right: 0; bottom: 60px; width: 150px; height: 22px; }
  .firm-mark {
    position: absolute; left: 0; right: 0; top: 120px;
    display: flex; align-items: center; justify-content: center; gap: 14px;
  }
  .firm-mark__square { width: 40px; height: 40px; background: var(--orange); }
  .firm-mark__name {
    font-family: "Roboto Condensed", sans-serif; font-weight: 700;
    font-size: 26px; letter-spacing: .5px; color: var(--ink-dark);
  }
  .firm-tagline {
    position: absolute; left: 0; right: 0; top: 172px; text-align: center;
    font-family: "Roboto Condensed", sans-serif; font-size: 13px;
    letter-spacing: 5px; color: var(--ink);
  }
  .practice-areas {
    position: absolute; left: 0; right: 0; bottom: 28px;
    display: flex; justify-content: center; gap: 22px;
    font-size: 11px; color: var(--ink-dark);
  }
  .practice-areas li { list-style: none; display: flex; align-items: center; gap: 7px; }
  .practice-areas li::before { content: ""; width: 8px; height: 8px; background: var(--orange); }

  /* Back */
  .card--back .band--tab { left: 292px; top: 0; width: 22px; height: 140px; border-radius: 0 0 11px 11px; }
  .person-icon { position: absolute; left: 295px; top: 116px; }
  .back-brand {
    position: absolute; left: 36px; bottom: 40px;
    display: flex; align-items: center; gap: 14px;
  }
  .back-brand__square { width: 46px; height: 46px; background: var(--orange); }
  .back-brand__text { border-left: 2px solid var(--ink); padding-left: 10px; }
  .back-brand__name {
    font-family: "Roboto Condensed", sans-serif; font-weight: 700;
    font-size: 22px; line-height: 1.05; color: var(--ink);
  }
  .back-brand__tagline {
    font-family: "Roboto Condensed", sans-serif; font-size: 11px;
    letter-spacing: 2px; color: var(--orange); margin-top: 4px;
  }
  .holder { position: absolute; left: 336px; top: 34px; }
  .holder__name {
    font-family: "Roboto Condensed", sans-serif; font-weight: 700; font-size: 26px;
    color: var(--ink);
  }
  .holder__name span { color: var(--orange); }
  .holder__title { font-size: 12px; letter-spacing: 1px; color: var(--ink); }
  .contacts { position: absolute; left: 336px; top: 118px; list-style: none; }
  .contacts li {
    display: flex; align-items: flex-start; gap: 14px;
    font-size: 14px; line-height: 1.35; color: var(--ink-dark); margin-bottom: 12px;
  }
  .contacts .icon { flex: none; width: 24px; height: 24px; }
</style>
</head>
<body>

<section class="card card--front" aria-label="Card front">
  <div class="card__texture" role="img" aria-label="Light grey faceted texture"></div>
  <div class="band band--top"></div>
  <div class="band band--bottom"></div>
  <div class="firm-mark">
    <div class="firm-mark__square"></div>
    <div class="firm-mark__name">HALBROOK, TESSING &amp; ORLOW, LLP</div>
  </div>
  <div class="firm-tagline">ATTORNEYS AT LAW</div>
  <ul class="practice-areas">
    <li>Real estates and Construction</li>
    <li>Business Disputes</li>
    <li>Trial Litigation/Appeals</li>
  </ul>
</section>

<section class="card card--back" aria-label="Card back">
  <div class="card__texture" role="img" aria-label="Light grey faceted texture"></div>
  <div class="band band--tab"></div>
  <svg class="person-icon" width="16" height="18" viewBox="0 0 16 18" aria-hidden="true">
    <circle cx="8" cy="5" r="4" fill="#fff"/>
    <path d="M1 17c0-4 3-7 7-7s7 3 7 7z" fill="#fff"/>
  </svg>

  <div class="back-brand">
    <div class="back-brand__square"></div>
    <div class="back-brand__text">
      <div class="back-brand__name">HALBROOK<br>TESSING<br>ORLOW</div>
      <div class="back-brand__tagline">ATTORNEYS AT LAW</div>
    </div>
  </div>

  <div class="holder">
    <div class="holder__name"><span>DANA</span> R. TESSING</div>
    <div class="holder__title">PARTNER</div>
  </div>

  <ul class="contacts">
    <li>
      <svg class="icon" viewBox="0 0 24 24" aria-hidden="true">
        <circle cx="12" cy="12" r="12" fill="var(--orange)"/>
        <path d="M8 6.5l2 0 1 3-1.5 1a7 7 0 0 0 4 4l1-1.5 3 1v2a1.5 1.5 0 0 1-1.5 1.5A10 10 0 0 1 6.5 8 1.5 1.5 0 0 1 8 6.5z" fill="#fff"/>
      </svg>
      <span>012 555 0142<br>012 555 0142</span>
    </li>
    <li>
      <svg class="icon" viewBox="0 0 24 24" aria-hidden="true">
        <circle cx="12" cy="12" r="12" fill="var(--orange)"/>
        <g fill="none" stroke="#fff" stroke-width="1.3">
          <circle cx="12" cy="12" r="6"/>
          <ellipse cx="12" cy="12" rx="2.6" ry="6"/>
          <line x1="6" y1="12" x2="18" y2="12"/>
        </g>
      </svg>
      <span>info@htolaw.com<br>www.htolaw.com</span>
    </li>
    <li>
      <svg class="icon" viewBox="0 0 24 24" aria-hidden="true">
        <circle cx="12" cy="12" r="12" fill="var(--orange)"/>
        <path d="M12 5a4.5 4.5 0 0 0-4.5 4.5C7.5 13 12 18.5 12 18.5s4.5-5.5 4.5-9A4.5 4.5 0 0 0 12 5z" fill="#fff"/>
        <circle cx="12" cy="9.5" r="1.7" fill="var(--orange)"/>
      </svg>
      <span>1450 Corran Street<br>Tellwick, AK 99850</span>
    </li>
  </ul>
</section>

</body>
</html>
```